Vesk Architecture

We are a architectural design and build company working between scales 1/1000 to 1/1 we want people to understand our difference from our design experience and quality.we build hotels restourants and office spaces.Our company name is Vesk architecture to mind sustainability.

We want to write our adress phone and work spesifications on the card and we want our logo as backround.

Ps:you could find the logo adress and phone box numbers from the web:www.veskmimarlik-ornek.com

Target Market(s)

Who looks for experts.

Industry/Entity Type

Architecture

Requirements
Must have
• Design is over everything.
Should not have
• we don want it to be colorfull

```html
<!DOCTYPE html>
<html lang="en">
<head>
<meta charset="utf-8">
<title>Vesk Architecture – Business Card</title>
<link rel="stylesheet" href="https://fonts.googleapis.com/css2?family=Arimo:wght@700&display=swap">
<style>
  :root {
    --brown-deep: #6a4e3c;
    --brown-mid: #7d604c;
    --brown-soft: #97796a;
    --city-light: #dfe2e2;
    --city-grey: #9aa09f;
    --ink-white: #ffffff;
  }
  html, body {
    margin: 0;
    padding: 0;
    width: 1200px;
    height: 685px;
    overflow: hidden;
    background: #ffffff;
  }
  .card {
    position: relative;
    width: 1200px;
    height: 685px;
    overflow: hidden;
    background: linear-gradient(180deg, var(--brown-soft) 0%, var(--brown-mid) 55%, var(--brown-deep) 100%);
    font-family: "Arimo", Arial, sans-serif;
    font-weight: 700;
    color: var(--ink-white);
  }
  .city-photo {
    position: absolute;
    top: 0;
    left: 0;
    width: 1200px;
    height: 250px;
    background: linear-gradient(180deg, var(--city-light) 0%, var(--city-grey) 70%, var(--brown-soft) 100%);
  }
  .brand-name {
    position: absolute;
    top: 70px;
    left: 0;
    width: 1200px;
    margin: 0;
    text-align: center;
    font-size: 240px;
    line-height: 1;
    letter-spacing: 4px;
    color: var(--ink-white);
  }
  .work-specs {
    position: absolute;
    top: 340px;
    left: 0;
    width: 1200px;
    margin: 0;
    text-align: center;
    font-size: 30px;
    line-height: 1;
    letter-spacing: 3px;
    color: var(--ink-white);
  }
  .contact {
    position: absolute;
    left: 0;
    width: 1200px;
    top: 462px;
    margin: 0;
    text-align: center;
    font-style: normal;
    font-size: 42px;
    line-height: 52px;
    letter-spacing: 1px;
    text-shadow: 1px 2px 2px rgba(40, 25, 15, 0.55);
  }
  .contact-line { display: block; white-space: pre; }
</style>
</head>
<body>
  <main class="card">
    <div class="city-photo" role="img" aria-label="Photograph of a city skyline with high-rise apartment towers"></div>

    <h1 class="brand-name">vesk</h1>

    <p class="work-specs">DESIGN &amp; BUILD · HOTELS · RESTAURANTS · OFFICES</p>

    <address class="contact">
      <span class="contact-line">Lale Mah. Ada Cad. Defne Sok.</span>
      <span class="contact-line">No:7 Ada Kadikoy/Istanbul</span>
      <span class="contact-line">T.0216 555 01 47    F.0216 555 01 48</span>
      <span class="contact-line">E-mail:veskmimarlik@ornek-posta.com</span>
    </address>
  </main>
</body>
</html>
```